Design of business signage for outside store front

We need signage designed for outside a store front.  We already have a logo, colours and font that we would like to use but would like some ideas as regards layout/design of the signage.  The final product will be for the use of the installer to produce and install the signage.  Attached are files with our logo and font and a picture of the current signage which needs to be replaced.  The size and shape of the signage will be the same as the current signage, its just the design/layout that we would like changed.
N.B. We would like two versions if possible, one with the web address and one without the web address to see what they look like.

```html
<!DOCTYPE html>
<html lang="en">
<head>
<meta charset="utf-8">
<title>Tierra Dorada – Storefront Signage Options</title>
<link rel="stylesheet" href="https://fonts.googleapis.com/css2?family=Montserrat:wght@400;500;800&display=swap">
<style>
  :root {
    --wine: #8b2533;
    --gold: #f2cd30;
    --ink: #1f1f1f;
    --paper: #ffffff;
    --backdrop: #a1a5af;
  }
  * { margin: 0; padding: 0; box-sizing: border-box; }
  html, body { width: 1200px; height: 876px; overflow: hidden; }
  body {
    background: var(--backdrop);
    font-family: "Montserrat", Arial, sans-serif;
    position: relative;
  }
  .sign {
    position: absolute;
    left: 200px;
    width: 800px;
    height: 400px;
    background: var(--paper);
  }
  .sign--with-web { top: 26px; }
  .sign--plain { top: 450px; }

  .sign__panel {
    position: absolute;
    left: 0; top: 0;
    width: 229px; height: 100%;
    background: var(--wine);
  }
  .sign__frame {
    position: absolute;
    left: 229px; top: 0;
  }
  .sign__brand {
    position: absolute;
    left: 268px;
    color: var(--wine);
    font-weight: 800;
    line-height: 1;
    white-space: nowrap;
  }
  .sign__brand-main {
    top: 96px;
    font-size: 104px;
    letter-spacing: 1px;
  }
  .sign__brand-sub {
    top: 200px;
    font-size: 62px;
    letter-spacing: 27px;
  }
  .sign__tagline {
    position: absolute;
    left: 270px;
    top: 270px;
    font-size: 27px;
    font-weight: 500;
    letter-spacing: 6.5px;
    color: var(--ink);
    white-space: nowrap;
  }
  .sign__web {
    position: absolute;
    left: 383px;
    top: 349px;
    width: 247px;
    text-align: center;
    font-size: 19px;
    font-weight: 400;
    color: var(--wine);
    white-space: nowrap;
  }
</style>
</head>
<body>

  <section class="sign sign--with-web" aria-label="Signage option with web address">
    <div class="sign__panel"></div>
    <svg class="sign__frame" width="571" height="400" viewBox="0 0 571 400" aria-hidden="true">
      <path d="M0 38 H519 Q537 38 537 56 V344 Q537 362 519 362 H450"
            fill="none" stroke="var(--wine)" stroke-width="2.4"/>
      <path d="M0 362 H139" fill="none" stroke="var(--wine)" stroke-width="2.4"/>
    </svg>
    <div class="sign__brand sign__brand-main">TIERRA</div>
    <div class="sign__brand sign__brand-sub">DORADA</div>
    <p class="sign__tagline">Spanish Artisan foods</p>
    <p class="sign__web">www.tierradorada.com.au</p>
  </section>

  <section class="sign sign--plain" aria-label="Signage option without web address">
    <div class="sign__panel"></div>
    <div class="sign__brand sign__brand-main">TIERRA</div>
    <div class="sign__brand sign__brand-sub">DORADA</div>
    <p class="sign__tagline">Spanish Artisan foods</p>
  </section>

</body>
</html>
```